New young doctors office business card

Doctor's office
Hello:
My name is Dr. Mateo Anselmo Quiroga Benítez. I need a business card for my new office located within a hospital. The name of the hospital is "Hospital Almendral". Although the hospital logo and name must be included in the business card, please make me a personal logo for myself. The logo might be maybe my name in a stylish font, or my initials (MAQB) or something like that. Im more inclined to a font logo, rather than a image logo, but a good one might change my mind. The info on my business card is going to be in spanish. The following info must be included please (the info within parenthesis is not to be included, it is provided for you to understand it since it's in spanish, so you can properly place it on the card):
-Dr. Mateo Anselmo Quiroga Benítez (my name)
-Medicina general (My specialty)
-Hospital Almendral (The name of the hospital where my office is)
-Calle Tomás Ibarrola #527 Col. Peñascal (address)
-Tel 471-5836 (Office phone)
-Sábado y domingo 10:00 am a 10:00pm (Office hours)
-Emergencias: 613-907-5148 (Emergency phone)
-mateoqb@correoandino.net (email)
-English Spoken
So, that's all the info i need to be on the business card. Although it's a business card for a doctor's office, i dont want it to be a boring, plain business card. Make it eye-catchy and stylish please. As i said, the hospital logo must be included. You'll find it on the heading of the PDF file i attached, but dont make it the center of attention.
Physician
Hello:My name is Dr. Mateo Anselmo Quiroga Benítez. I need a business card for my new office located within a hospital. The name of the hospital is "Hospital Almendral". Although the hospital logo and name must be included in the business card, please make me a personal logo for myself. The logo might be maybe my name in a stylish font, or my initials (MAQB) or something like that. Im more inclined to a font logo, rather than a image logo, but a good one might change my mind. The info on my business card is going to be in spanish. The following info must be included please (the info within parenthesis is not to be included, it is provided for you to understand it since it's in spanish, so you can properly place it on the card):-Dr. Mateo Anselmo Quiroga Benítez (my name)-Medicina general (My specialty)-Hospital Almendral (The name of the hospital where my office is)-Calle Tomás Ibarrola #527 Col. Peñascal (address)-Tel 471-5836 (Office phone)-Sábado y domingo 10:00 am a 10:00pm (Office hours)-Emergencias: 613-907-5148 (Emergency phone)-mateoqb@correoandino.net (email)-English Spoken So, that's all the info i need to be on the business card. Although it's a business card for a doctor's office, i dont want it to be a boring, plain business card. Make it eye-catchy and stylish please. As i said, the hospital logo must be included. You'll find it on the heading of the PDF file i attached, but dont make it the center of attention.

```html
<!DOCTYPE html>
<html lang="es">
<head>
<meta charset="utf-8">
<title>Tarjeta de presentación — Dr. Mateo Anselmo Quiroga Benítez</title>
<link rel="stylesheet" href="https://fonts.googleapis.com/css2?family=Jost:wght@400;500;700&family=Yellowtail&display=swap">
<style>
  :root {
    --backdrop: #3b3b3b;
    --card-grey: #5f6060;
    --ink-white: #ffffff;
    --gold: #e2b32a;
    --hospital-blue: #1f2f8f;
    --coat-white: #f1f1f1;
    --shirt-lavender: #a9acd9;
    --figure-dark: #3f4040;
  }
  * { margin: 0; padding: 0; box-sizing: border-box; }
  html, body {
    width: 1200px; height: 816px; overflow: hidden;
    background: var(--backdrop);
    font-family: "Jost", "Futura", sans-serif;
  }
  .canvas { position: relative; width: 1200px; height: 816px; }

  .card {
    position: absolute;
    width: 255px; height: 443px;
    left: 484px;
    transform: rotate(90deg);
    overflow: hidden;
    background: var(--card-grey);
    color: var(--ink-white);
  }
  .card--front { top: 39px; }
  .card--back { top: 326px; }

  /* Front */
  .front-artwork {
    position: absolute; inset: 0;
    background: linear-gradient(to bottom,
      var(--coat-white) 0%, #e6e6ea 22%, var(--shirt-lavender) 30%,
      #7f83a8 35%, #5a5b5e 37%, var(--figure-dark) 70%, #4c4c4c 100%);
  }
  .hospital-tag {
    position: absolute;
    font-weight: 700; color: var(--hospital-blue);
    line-height: 1.05; text-align: center;
  }
  .card--front .hospital-tag { left: 40px; top: 126px; font-size: 8px; width: 40px; }
  .personal-mark {
    position: absolute; left: 0; right: 0; top: 168px;
    text-align: center;
    font-size: 50px; font-weight: 500; letter-spacing: 12px;
    color: var(--gold);
  }
  .doctor-name {
    position: absolute; left: 34px; top: 306px;
    font-size: 23px; font-weight: 400; line-height: 1.1;
  }
  .specialty-script {
    position: absolute; left: 8px; top: 370px;
    font-family: "Yellowtail", cursive;
    font-size: 34px; color: var(--gold);
  }

  /* Back */
  .next-visit-title {
    position: absolute; left: 48px; top: 12px;
    font-size: 21px; font-weight: 700; letter-spacing: 0.5px;
  }
  .field-label {
    position: absolute; left: 14px;
    font-size: 9px; font-weight: 500;
  }
  .field-label--date { top: 46px; }
  .field-label--notes { top: 68px; }
  .field-box { position: absolute; left: 53px; width: 184px; border: 1.5px solid var(--gold); }
  .field-box--date { top: 43px; height: 20px; }
  .field-box--notes { top: 70px; height: 119px; }
  .specialty {
    position: absolute; left: 28px; top: 197px;
    font-size: 23px; font-weight: 400;
  }
  .contact-list {
    position: absolute; left: 10px; top: 232px; width: 235px;
    list-style: none; font-size: 10.5px; line-height: 1.4;
  }
  .contact-list li { display: flex; align-items: flex-start; gap: 6px; margin-bottom: 4px; }
  .contact-list svg { flex: none; width: 13px; height: 13px; margin-top: 1px; }
  .card--back .hospital-tag { left: 150px; top: 388px; width: 70px; font-size: 13px; }
</style>
</head>
<body>
<main class="canvas">

  <section class="card card--front" aria-label="Frente de la tarjeta">
    <div class="front-artwork" role="img" aria-label="Ilustración de un médico con bata blanca, camisa lavanda y estetoscopio"></div>
    <div class="hospital-tag">Hospital Almendral</div>
    <div class="personal-mark">MAQB</div>
    <h1 class="doctor-name">Dr. Mateo Anselmo<br>Quiroga Benítez</h1>
    <p class="specialty-script">Medicina General</p>
  </section>

  <section class="card card--back" aria-label="Reverso de la tarjeta">
    <h2 class="next-visit-title">Próxima cita:</h2>
    <span class="field-label field-label--date">Fecha:</span>
    <div class="field-box field-box--date"></div>
    <span class="field-label field-label--notes">Notas:</span>
    <div class="field-box field-box--notes"></div>
    <h3 class="specialty">Medicina general</h3>
    <ul class="contact-list">
      <li>
        <svg viewBox="0 0 14 14" fill="none" stroke="#e2b32a" stroke-width="1.5"><path d="M7 13s5-4.5 5-8A5 5 0 0 0 2 5c0 3.5 5 8 5 8z"/><circle cx="7" cy="5" r="1.8"/></svg>
        <span>Hospital Almendral Calle Tomás Ibarrola #527 Col. Peñascal</span>
      </li>
      <li>
        <svg viewBox="0 0 14 14" fill="none" stroke="#e2b32a" stroke-width="1.5"><rect x="1" y="2" width="12" height="10"/><path d="M4 2v10M10 2v10"/></svg>
        <span>Oficina: 471-5836<br>Emergencias: 613-907-5148</span>
      </li>
      <li>
        <svg viewBox="0 0 14 14"><circle cx="7" cy="7" r="6" fill="#e2b32a"/><path d="M7 3.5V7h3" stroke="#5f6060" stroke-width="1.4" fill="none"/></svg>
        <span>sábado y domingo 10:00am -10:00pm</span>
      </li>
      <li>
        <svg viewBox="0 0 14 14" fill="none" stroke="#e2b32a" stroke-width="1.4"><rect x="1" y="2.5" width="12" height="9"/><path d="M1 2.5l6 5 6-5"/></svg>
        <span>mateoqb@correoandino.net</span>
      </li>
    </ul>
    <div class="hospital-tag">Hospital Almendral</div>
  </section>

</main>
</body>
</html>
```